Corporate Design für Elektrotechnik-Unternehmen
Zielgruppe
Unser junges Elektrotechnik-Unternehmen ist spezialisiert auf den Bau hochwertiger, individueller Schaltschränke, die präzise auf die Anforderungen unserer Kunden zugeschnitten sind.
Zusätzlich übernehmen wir fachgerechte Reparaturen sowie die Fertigung einzigartiger Sonderlösungen in höchster handwerklicher Qualität.
Unsere Zielgruppe umfasst vor allem industrielle Kunden, die zuverlässige, maßgeschneiderte Elektrotechnik benötigen, aber auch private Auftraggeber, die Wert auf Qualität und individuell gefertigte Lösungen legen.
Aufgabenstellung
Das Design soll Präzision, Kompetenz und höchste Qualität vermitteln und insgesamt professionell, klar strukturiert und technisch wirken.
Die Bildwelt sollte industrielle Komponenten, Schaltschränke und Fertigungsprozesse zeigen, jedoch nicht in Richtung allgemeiner Hauselektrik gehen, da dies nicht unser Schwerpunkt ist.
In der Bildsprache können klassische handwerkliche Symbole wie Glühlampen, Schaltzeichen oder ähnliche technisch bekannte Elemente genutzt werden – dezent eingesetzt und passend zum handwerklichen Charakter.
Das Erscheinungsbild muss vielseitig einsetzbar sein – von Website über Fahrzeugbeschriftung bis zu Arbeitskleidung – und sollte keine zu feinen oder übermäßig komplexen Elemente enthalten.
Gleichzeitig soll das Design eine starke, wiedererkennbare Markenwirkung haben, modern wirken und auch in einfarbigen Varianten gut funktionieren.

```html
<!DOCTYPE html>
<html lang="de">
<head>
<meta charset="utf-8">
<title>Schaltwerk Lindenau – Briefbogen</title>
<link href="https://fonts.googleapis.com/css2?family=Montserrat:wght@400;500;700&display=swap" rel="stylesheet">
<style>
  :root {
    --brand-red: #e20a17;
    --ink: #1d1d1b;
    --rule: #9a9a9a;
    --sign-blue: #2a6fb8;
    --paper: #ffffff;
  }
  * { margin: 0; padding: 0; box-sizing: border-box; }
  html, body { width: 849px; height: 1200px; overflow: hidden; background: var(--paper); }
  body { font-family: "Montserrat", Arial, sans-serif; color: var(--ink); }
  .sheet {
    position: relative; width: 849px; height: 1200px;
    border: 1px solid #b5b5b5; overflow: hidden; background: var(--paper);
  }
  .corner-accent { position: absolute; top: 0; right: 0; }
  .brand {
    position: absolute; left: 474px; top: 58px;
    display: flex; align-items: center; gap: 14px;
  }
  .brand-mark { width: 44px; height: 44px; background: var(--brand-red); }
  .brand-name {
    font-weight: 700; font-size: 21px; line-height: 1.25;
    letter-spacing: 1.2px; text-transform: uppercase; color: var(--ink);
  }
  .sender-line { position: absolute; left: 103px; top: 207px; font-size: 10px; }
  .letter-body {
    position: absolute; left: 104px; top: 433px; width: 667px;
    font-size: 14.4px; line-height: 18.6px;
  }
  .salutation { margin-bottom: 18px; font-size: 15px; }
  .paragraph { text-align: justify; margin-bottom: 18.6px; hyphens: manual; }
  .closing { position: absolute; left: 104px; top: 693px; font-size: 15px; }
  .signature {
    position: absolute; left: 104px; top: 719px; width: 311px; height: 38px;
    background: linear-gradient(90deg, rgba(42,111,184,0.18), rgba(42,111,184,0.06));
    border-radius: 4px;
  }
  .signer-name { position: absolute; left: 104px; top: 786px; font-size: 15px; }
  .footer-info { position: absolute; left: 0; top: 1098px; width: 849px; height: 66px; font-size: 11.5px; line-height: 14.5px; }
  .footer-col { position: absolute; top: 0; }
  .footer-divider { position: absolute; top: 0; width: 1px; height: 66px; background: var(--rule); }
  .footer-row { display: flex; align-items: flex-start; gap: 10px; }
  .footer-icon { flex: none; width: 17px; height: 17px; }
  .bottom-band { position: absolute; left: 0; bottom: 0; }
</style>
</head>
<body>
<main class="sheet">
  <svg class="corner-accent" width="94" height="92" viewBox="0 0 94 92" aria-hidden="true">
    <polygon points="0,0 94,0 94,92" fill="var(--brand-red)"/>
  </svg>

  <header class="brand">
    <div class="brand-mark" aria-hidden="true"></div>
    <div class="brand-name">Schaltwerk<br>Lindenau</div>
  </header>

  <p class="sender-line">Adresse&nbsp; Lorem ipsum dolor sit amet, elitrinvidun</p>

  <section class="letter-body">
    <p class="salutation">Sehr geehrte Damen ubd Herren</p>
    <p class="paragraph">dolor sit amet, consetetur sadipscing elitr, sed diam nonumy eirmod tempor invidunt ut labore et dolore magna aliquyam erat, sed diam voluptua. At vero eos et accusam et justo duo dolores et ea rebum. labore et dolore magna aliquyam</p>
    <p class="paragraph">dolor sit amet, consetetur sadipscing elitr, sed diam nonumy eirmod tempor invidunt ut labore et dolore magna aliquyam erat, sed diam voluptua. At vero eos et accusam et justo dolor sit amet, consetetur sadipscing elitr, sed diam nonumy eirmod tempor invid-unt ut&nbsp; duo dolores et ea rebum.labore et dolore magna aliquyam erat, sed diam volup-tua. At vero eos et accusam et justo dolor</p>
  </section>

  <p class="closing">Mit freundlichen Grüßen</p>
  <div class="signature" role="img" aria-label="Handschriftliche Unterschrift in blauer Tinte"></div>
  <p class="signer-name">Jonas Feldbruck</p>

  <footer class="footer-info">
    <div class="footer-col" style="left:106px;">
      <div class="footer-row">
        <svg class="footer-icon" viewBox="0 0 20 20" aria-hidden="true">
          <circle cx="10" cy="10" r="9" fill="none" stroke="var(--ink)" stroke-width="1.5"/>
          <path d="M10 4.5a3.2 3.2 0 0 0-3.2 3.2c0 2.4 3.2 6.3 3.2 6.3s3.2-3.9 3.2-6.3A3.2 3.2 0 0 0 10 4.5z" fill="var(--ink)"/>
          <circle cx="10" cy="7.7" r="1.2" fill="#fff"/>
        </svg>
        <span>sed diam nonumy eirmodnvid-<br>unt ut labore et dolore magna</span>
      </div>
    </div>
    <div class="footer-divider" style="left:328px;"></div>
    <div class="footer-col" style="left:360px;">
      <div class="footer-row">
        <svg class="footer-icon" viewBox="0 0 20 20" aria-hidden="true">
          <circle cx="10" cy="10" r="9" fill="none" stroke="var(--ink)" stroke-width="1.5"/>
          <path d="M7 5.5l1.6 2.3-1 1.1c.6 1.3 1.5 2.2 2.8 2.8l1.1-1 2.3 1.6-.9 1.6c-3.4-.3-6.5-3.4-6.8-6.8z" fill="var(--ink)"/>
        </svg>
        <span>071 204 58 36</span>
      </div>
      <div class="footer-row" style="margin-top:12px;">
        <svg class="footer-icon" viewBox="0 0 20 20" aria-hidden="true">
          <circle cx="10" cy="10" r="9" fill="none" stroke="var(--ink)" stroke-width="1.5"/>
          <text x="10" y="13.5" text-anchor="middle" font-family="Montserrat, Arial, sans-serif" font-weight="700" font-size="10" fill="var(--ink)">@</text>
        </svg>
        <span>unt ut labore et</span>
      </div>
    </div>
    <div class="footer-divider" style="left:506px;"></div>
    <div class="footer-col" style="left:530px;">
      <div class="footer-row">
        <svg class="footer-icon" viewBox="0 0 20 20" aria-hidden="true">
          <circle cx="10" cy="10" r="9" fill="none" stroke="var(--ink)" stroke-width="1.5"/>
          <circle cx="10" cy="10" r="5" fill="none" stroke="var(--ink)" stroke-width="1"/>
          <path d="M5 10h10M10 5v10M10 5c-2 2.5-2 7.5 0 10M10 5c2 2.5 2 7.5 0 10" fill="none" stroke="var(--ink)" stroke-width="0.9"/>
        </svg>
        <span>Bankverbindung&nbsp;&nbsp;&nbsp; ed diam nonumy<br>eirmod tempor invidunt ut labore et<br>dolore magna aliquyam</span>
      </div>
    </div>
  </footer>

  <svg class="bottom-band" width="849" height="24" viewBox="0 0 849 24" aria-hidden="true">
    <polygon points="0,0 110,0 132,24 0,24" fill="var(--brand-red)"/>
    <polygon points="134,0 365,0 388,24 134,24" fill="var(--brand-red)"/>
    <polygon points="389,0 537,0 560,24 389,24" fill="var(--brand-red)"/>
    <polygon points="561,0 849,0 849,24 561,24" fill="var(--brand-red)"/>
  </svg>
</main>
</body>
</html>
```